Take my 1-Page Consulting Service Introduction to the next level!

I am looking for a designer to enhance my current 1-Page Consulting Services Introduction.

My business - Bright Harbor Services - offers HR consulting to companies looking to be more people-centric. The design should be professional, but also convey a sense of "sparking people" or inspiring people to engage and excel.

The new Word document will:
* Use my new business logo, logo icon and colors. (files attached)
* Include my head shot (file attached)
* Impress potential clients by improving the visual appeal
* Be easy for me to update in Word (small edits)

Target Market(s)

Business owners and senior leaders

Font styles to use
Sans Serif

Requirements
Must have
• My head shot (can be cropped) , my logo
Nice to have
• use of my logo icon or parts of it (if that works for the design)

```html
<!DOCTYPE html>
<html lang="en">
<head>
<meta charset="utf-8">
<title>Bright Harbor Services – Dana Whitlock</title>
<link rel="stylesheet" href="https://fonts.googleapis.com/css2?family=Roboto:ital,wght@0,300;0,400;0,500;0,700;1,300&display=swap">
<style>
  :root{
    --navy:#00264f;
    --blue:#0071bc;
    --blue-dark:#00528f;
    --ink:#0d2a57;
    --link:#0a6fc2;
    --white:#ffffff;
    --panel-a:#e4eef7;
    --panel-b:#cfe1f0;
    --photo-a:#c9c6b8;
    --photo-b:#4e5560;
  }
  *{margin:0;padding:0;box-sizing:border-box}
  html,body{width:927px;height:1200px;overflow:hidden;background:var(--white)}
  body{font-family:"Roboto",Arial,sans-serif;color:var(--ink);position:relative}
  .sheet{position:relative;width:927px;height:1200px;overflow:hidden;background:var(--white)}

  /* header */
  .brand{position:absolute;left:62px;top:62px;display:flex;align-items:center;gap:12px}
  .brand-dot{width:22px;height:22px;border-radius:50%;background:var(--blue)}
  .brand-name{font-size:27px;font-weight:700;color:var(--navy);line-height:1.1;width:220px}
  .contact{position:absolute;left:539px;top:47px;list-style:none}
  .contact li{display:flex;align-items:center;height:36px;font-size:18px;color:var(--ink)}
  .contact svg{width:20px;height:20px;margin-right:15px;flex:none}

  /* bands */
  .band-top{position:absolute;left:0;top:180px;width:927px;height:34px;background:var(--navy)}
  .name-bar{position:absolute;left:0;top:180px;width:349px;height:75px;background:var(--navy)}
  .name{position:absolute;left:62px;top:192px;font-size:38px;font-weight:500;color:var(--white);letter-spacing:.2px}
  .intro-side{position:absolute;left:0;top:254px;width:349px;height:289px;background:var(--blue)}
  .intro-shade{position:absolute;left:0;top:254px;width:349px;height:289px}
  .portrait{position:absolute;left:18px;top:275px;width:310px;height:246px;background:linear-gradient(160deg,var(--photo-a),#9a9a95 45%,var(--photo-b))}
  .intro{position:absolute;left:349px;top:213px;width:578px;height:330px;background:var(--white);padding:22px 40px 0 32px;font-size:17.5px;line-height:21.8px;font-weight:500}
  .intro p+p{margin-top:21.8px}
  .intro a{color:var(--link);text-decoration:none}

  .section-band{position:absolute;left:0;top:543px;width:927px;height:46px;background:var(--navy)}
  .section-title{position:absolute;left:379px;top:549px;font-size:28.5px;font-weight:500;color:var(--white)}

  /* services column */
  .services{position:absolute;left:0;top:589px;width:349px;height:611px;background:var(--blue);overflow:hidden}
  .services-shade{position:absolute;left:0;top:0}
  .service-list{position:absolute;left:0;top:0;list-style:none;width:349px}
  .service{position:absolute;left:22px;display:flex;align-items:center;height:36px;font-size:18.5px;font-weight:500;color:var(--white)}
  .service-icon{width:34px;height:34px;border-radius:6px;background:rgba(255,255,255,.22);margin-right:22px;flex:none}

  /* experience */
  .timeline{position:absolute;left:386px;top:589px;width:1px;height:296px;background:var(--ink)}
  .roles{position:absolute;left:380px;top:604px;list-style:none}
  .role{position:relative;height:59.4px;padding-left:38px}
  .role::before{content:"";position:absolute;left:2px;top:9px;width:8px;height:8px;background:var(--ink);transform:rotate(45deg)}
  .role-title{font-size:18px;font-weight:500;line-height:22px}
  .role-org{font-size:15px;font-style:italic;font-weight:300;line-height:22px}
  .credentials{position:absolute;left:381px;top:905px;width:520px;font-size:17.5px;line-height:21.8px;font-weight:500}

  /* value panels */
  .values{position:absolute;left:349px;top:1019px;width:578px;height:181px;display:flex}
  .value{width:193px;height:181px;background:var(--panel-a);display:flex;flex-direction:column;align-items:center;padding-top:30px;text-align:center;font-size:12px;line-height:14.5px;color:var(--ink)}
  .value:nth-child(2){background:var(--panel-b);border-left:1.5px dashed var(--ink);border-right:1.5px dashed var(--ink);width:192px}
  .value-icon{width:54px;height:50px;border-radius:8px;background:#b5cde3;margin-bottom:19px}
  .value p{width:150px}
</style>
</head>
<body>
<div class="sheet">

  <header>
    <div class="brand"><span class="brand-dot"></span><span class="brand-name">Bright Harbor Services</span></div>
    <ul class="contact">
      <li><svg viewBox="0 0 20 20"><rect width="20" height="20" rx="4" fill="#00264f"/><rect x="4" y="6" width="12" height="8" fill="none" stroke="#fff" stroke-width="1.3"/><path d="M4 6l6 5 6-5" fill="none" stroke="#fff" stroke-width="1.3"/></svg>dwhitlock@brightharborservices.com</li>
      <li><svg viewBox="0 0 20 20"><rect width="20" height="20" rx="4" fill="#00264f"/><path d="M10 4a4 4 0 0 1 4 4c0 3-4 8-4 8s-4-5-4-8a4 4 0 0 1 4-4z" fill="#fff"/><circle cx="10" cy="8" r="1.5" fill="#00264f"/></svg>Port Alder, BC Canada</li>
      <li><svg viewBox="0 0 20 20"><rect width="20" height="20" rx="4" fill="#00264f"/><path d="M6 4.5l2.3 2.5-1.2 1.6c.8 1.8 2.3 3.3 4.1 4.1l1.6-1.2 2.5 2.3-1.5 1.9C9.5 15.5 4.5 10.5 4.3 6z" fill="#fff"/></svg>555.014.2290</li>
    </ul>
  </header>

  <div class="band-top"></div>
  <div class="name-bar"></div>
  <h1 class="name">Dana Whitlock</h1>
  <div class="intro-side"></div>
  <svg class="intro-shade" width="349" height="289" viewBox="0 0 349 289"><polygon points="328,21 349,35 349,289 70,289 18,267 328,267" fill="#00528f"/></svg>
  <div class="portrait" role="img" aria-label="Head shot of the consultant"></div>

  <section class="intro">
    <p>Dana provides people strategy expertise that enables business growth and success. She’s known for change, learning, culture and performance systems that engage and empower.</p>
    <p>Dana partners with boards and leadership teams to convert vision into action and thrives on kick-starting business initiatives.&nbsp; She is a champion of people-centric decision-making with a wide range of industry experience. Dana fosters cultures that create meaningful in-person, hybrid and virtual team connection.&nbsp; She has dual US and Canadian citizenship and works cross-border with ease.<br><a href="#">www.example.com/in/danawhitlock</a></p>
  </section>

  <div class="section-band"></div>
  <h2 class="section-title">Professional Experience</h2>

  <aside class="services">
    <svg class="services-shade" width="349" height="70" viewBox="0 0 349 70"><polygon points="185,0 349,0 349,65" fill="#00528f"/></svg>
    <ul class="service-list">
      <li class="service" style="top:26px"><span class="service-icon" role="img" aria-label="Strategy icon"></span>People Strategies &amp; Execution</li>
      <li class="service" style="top:77px"><span class="service-icon" role="img" aria-label="Transformation icon"></span>Business Transformation</li>
      <li class="service" style="top:132px"><span class="service-icon" role="img" aria-label="Change icon"></span>Change Leadership</li>
      <li class="service" style="top:187px"><span class="service-icon" role="img" aria-label="Systems icon"></span>People Systems</li>
      <li class="service" style="top:241px"><span class="service-icon" role="img" aria-label="Leadership icon"></span>Leadership Development</li>
      <li class="service" style="top:296px"><span class="service-icon" role="img" aria-label="Team icon"></span>Personal &amp; Team Effectiveness</li>
      <li class="service" style="top:351px"><span class="service-icon" role="img" aria-label="Coaching icon"></span>Coaching</li>
      <li class="service" style="top:411px"><span class="service-icon" role="img" aria-label="Engagement icon"></span>Employee Engagement</li>
      <li class="service" style="top:461px"><span class="service-icon" role="img" aria-label="Learning icon"></span>Learning &amp; Development</li>
      <li class="service" style="top:514px"><span class="service-icon" role="img" aria-label="Execution icon"></span>People Strategies &amp; Execution</li>
    </ul>
  </aside>

  <div class="timeline"></div>
  <ol class="roles">
    <li class="role"><div class="role-title">Vice President, Development &amp; Culture|Learning</div><div class="role-org">Corvane Building Systems</div></li>
    <li class="role"><div class="role-title">Director, Restaurant Training &amp; Transformation</div><div class="role-org">Maple Grill Food Services of Canada</div></li>
    <li class="role"><div class="role-title">Director of Education</div><div class="role-org">Coastal Realty Professionals Association</div></li>
    <li class="role"><div class="role-title">Head of Virtual Communities</div><div class="role-org">Global Scholars Programme</div></li>
    <li class="role"><div class="role-title">Director of Academic Technology Services</div><div class="role-org">Ridgeview College</div></li>
  </ol>

  <p class="credentials">Dana holds a Masters of Arts in Education and Human Development.&nbsp; She is a certified Lumen© personal effectiveness coach, a certified Keystone Assessments coach and an experienced Shiftwise© Certified Change Practitioner.</p>

  <section class="values">
    <div class="value"><span class="value-icon" role="img" aria-label="Two people joining puzzle pieces"></span><p>Creating people strategies that engage, inspire and enable organizational growth and success.</p></div>
    <div class="value"><span class="value-icon" role="img" aria-label="Group of people with change arrows"></span><p>Change leadership that is inclusive, reduces barriers and accelerates transformation.</p></div>
    <div class="value"><span class="value-icon" role="img" aria-label="Presenter at a strategy board"></span><p>Organizational development that creates high performance and values alignment.</p></div>
  </section>

</div>
</body>
</html>
```